BrightLoop App Design

The attached document, [BrightLoop - Design & Requirements Document - v1.2], outlines the full design and functional requirements for the BrightLoop App. The key sections include:
• Company overview: Mission and vision statements
• High-level application overview
• App design guidelines
• App functional requirements
• Navigation information
To expedite app development, we are planning to use a Multi-Purpose PWA Mobile App Template. This template offers pre-built UI elements and layouts that are flexible and responsive, allowing for quicker development while maintaining a modern design.
Pixel Harbor Requirements:
We require designs for 11 app pages and 1 pop-up, as outlined in sections 3.13 and section 4 of the document. These designs should be delivered in Adobe format (as a minimum), ready to be handed over to our developers who will build the app using the template and corresponding code base.
Important Notes:
1. Leverage the Multi-Purpose PWA Mobile App Template: The designs must make use of the components and features available within the template. You can explore the template using the following link to view the pages, features, and styles:
o Template link: Varn: Multi-Purpose PWA Mobile App Template
2. Sample screens for Visual Reference: To aid in visualizing the app's navigation, please refer to the sample screens. This serves as a high-level guide to demonstrate the user flow but is not a literal requirement for the design.
o Note:
 Not all features and pages from the requirements document are represented in these screen samples
 The flow is provided purely to showcase the navigational paths within the app.

Deliverables:
The designs should align with the template's style, features, and UI components, with clear attention to how each page will function within the BrightLoop app. The final designs are expected to be in Adobe format for smooth developer handoff.
To confirm, we are looking to see how best to utilise the template design style etc for the APP’s final design, whilst incorporating all the requirements of the APP from the requirements document.

Target Market(s)

Young shopping demographic

Industry/Entity Type

Online Shopping

Requirements
Must have
• All the required pages designed
Nice to have
• See requirements document

```html
<!DOCTYPE html>
<html lang="en">
<head>
<meta charset="utf-8">
<title>BrightLoop App Screens</title>
<link href="https://fonts.googleapis.com/css2?family=Ubuntu:ital,wght@0,400;0,500;0,700;1,400&display=swap" rel="stylesheet">
<style>
:root{
  --canvas:#7f7f7f;
  --ink:#000;
  --text:#333;
  --muted:#999;
  --line:#d6d6d6;
  --soft:#f1f1f1;
  --green:#2fbf3f;
  --red:#e0342b;
  --c-coral:#f26464;
  --c-teal:#93d3c9;
  --c-slate:#3e4f5e;
  --photo-a:#cfcfcf;
  --photo-b:#8d8d8d;
}
*{box-sizing:border-box}
html,body{margin:0;width:1020px;height:1200px;overflow:hidden;background:var(--canvas);font-family:'Ubuntu',sans-serif;color:var(--text)}
.board{position:absolute;left:0;top:0;width:1764px;height:2075px;transform:scale(.5782);transform-origin:0 0}
.screen{position:absolute;width:275px;background:#fff;overflow:hidden}
.a{position:absolute}
.center{left:0;right:0;text-align:center}
.brand{position:absolute;left:0;right:0;top:35px;text-align:center;font-weight:700;font-size:17px;color:var(--ink)}
.title{position:absolute;left:0;right:0;top:86px;text-align:center;font-size:14px;font-weight:500;color:#4a4a4a;letter-spacing:.4px}
.intro{position:absolute;left:40px;width:195px;top:110px;text-align:center;font-size:8.6px;line-height:12.5px;color:#555}
.field{position:absolute;height:32px;border:1.5px solid var(--line);border-radius:17px;font-size:11px;color:#9d9d9d;padding-left:13px;line-height:29px;white-space:nowrap;overflow:hidden}
.btn{position:absolute;height:33px;line-height:33px;border-radius:17px;background:var(--ink);color:#fff;font-size:11px;font-weight:700;text-align:center;letter-spacing:.2px}
.btn-line{position:absolute;height:33px;line-height:30px;border-radius:17px;border:1.5px solid var(--ink);color:#000;font-size:11px;font-weight:500;text-align:center}
.links{position:absolute;left:0;right:0;text-align:center;font-size:8.5px;color:#444}
.links i{display:inline-block;width:1px;height:11px;background:#555;vertical-align:middle;margin:0 10px}
.social{position:absolute;width:172px;height:47px;border:1.5px solid #222;border-radius:4px}
.social .dot{position:absolute;left:20px;top:12px;width:22px;height:22px;border-radius:50%;background:#c8c8c8}
.social span{position:absolute;left:74px;top:10px;font-size:11px;font-weight:500;line-height:12.5px;color:#333;letter-spacing:.4px}
.check{position:absolute;width:16px;height:16px;border:1.5px solid #333;border-radius:3px}
.small{position:absolute;font-size:8.5px;color:#444}
.topbar{position:absolute;left:0;top:0;width:275px;height:44px;background:var(--ink)}
.topbar .brand{top:13px;color:#fff}
.topbar svg{position:absolute;right:21px;top:13px;width:18px;height:18px}
.label{position:absolute;font-size:8.5px;font-weight:700;color:#444;letter-spacing:.3px}
.photo{position:absolute;background:linear-gradient(160deg,var(--photo-a),#b8b8b8 45%,var(--photo-b))}
.nav{position:absolute;left:0;width:275px;height:46px;background:#fff;border-top:1px solid #eee}
.nav div{position:absolute;top:9px;width:90px;margin-left:-45px;text-align:center;font-size:8px;color:#999}
.nav div.on{color:#111}
.nav svg{display:block;margin:0 auto 2px;width:14px;height:14px}
.chip{position:absolute;height:25px;line-height:25px;border-radius:13px;background:var(--ink);color:#fff;font-size:8.2px;padding-left:14px;white-space:nowrap;overflow:hidden}
.sizes{position:absolute;display:flex;gap:7px}
.sizes span{width:35px;height:15px;border:1px solid var(--line);border-radius:8px;font-size:7px;color:#999;text-align:center;line-height:13px}
.swatch{position:absolute;width:17px;height:17px;border-radius:50%}
.tag{position:absolute;height:17px;line-height:17px;border-radius:9px;background:#777;color:#fff;font-size:8px;padding-left:26px}
.tabs{position:absolute;display:flex;gap:22px;font-size:8px;color:#bbb}
.tabs .on{color:#222;border-bottom:1px solid #222;padding-bottom:3px}
.desc{position:absolute;width:240px;font-size:8.5px;line-height:16.8px;color:#9a9a9a}
.ask{position:absolute;height:36px;border:1.5px solid #ccc;border-radius:18px}
.ask svg{position:absolute;right:0;top:-1px;width:35px;height:35px}
.buybar{position:absolute;left:0;width:275px;height:50px;display:flex}
.buybar div{flex:1;color:#fff;font-size:11px;font-weight:700;text-align:center;line-height:50px;background:#1d1d1d}
.buybar div+div{background:#000;border-left:1px solid #444}
.badge{position:absolute;left:0;height:32px;width:95px;background:var(--green);color:#fff;font-size:11px;font-weight:700;line-height:32px;padding-left:38px}
.badge::before{content:"";position:absolute;left:17px;top:9px;width:14px;height:14px;border-radius:50%;background:#fff}
.card{position:absolute;border:1px solid #ddd;border-radius:6px;background:#fff;overflow:hidden;box-shadow:0 1px 3px rgba(0,0,0,.12)}
.store{position:absolute;left:0;right:0;top:0;height:40px;border-bottom:1px solid #e4e4e4}
.radio{position:absolute;left:9px;top:11px;width:17px;height:17px;border:1.5px solid #444;border-radius:50%}
.avatar{position:absolute;left:36px;top:11px;width:18px;height:18px;border-radius:50%;background:#ddd}
.store b{position:absolute;left:60px;top:12px;font-size:11px;font-weight:400;color:#333}
.kebab{position:absolute;right:12px;top:11px;width:4px;height:18px}
.item{position:absolute;left:0;right:0}
.thumb{position:absolute;left:8px;width:44px;height:44px;border-radius:50%;background:radial-gradient(circle at 40% 40%,#d9d9d9,#777)}
.iname{position:absolute;left:62px;font-size:9px;color:#333}
.imeta{position:absolute;left:62px;font-size:6.5px;font-style:italic;color:#888}
.price{position:absolute;font-size:9px;font-weight:700;color:#111}
.step{position:absolute;display:flex;align-items:center}
.step .pm{width:19px;height:19px;border-radius:50%;background:#000;color:#fff;font-size:12px;line-height:18px;text-align:center;font-weight:700}
.step .qty{width:29px;height:19px;border:1px solid #ddd;font-size:7px;text-align:center;line-height:17px;color:#444}
.select{position:absolute;height:19px;border:1px solid #ccc;border-radius:10px;font-size:7px;color:#888;line-height:17px;padding-left:10px}
.select::after{content:"";position:absolute;right:9px;top:5px;width:4px;height:4px;border-right:1.5px solid #222;border-bottom:1.5px solid #222;transform:rotate(45deg)}
.totalbar{position:absolute;left:0;width:275px;height:48px;background:#000;border-radius:10px 10px 0 0;color:#fff;font-size:14px}
.totalbar span{position:absolute;top:15px}
.checkout{position:absolute;left:0;width:275px;height:45px;background:#000;color:#fff;font-size:11px;font-weight:700;text-align:center;line-height:45px;border-top:1px solid #333}
.swipe{position:absolute;background:var(--red)}
.swipe::after{content:"";position:absolute;left:17px;top:50%;width:19px;height:3px;background:#fff}
.pcard{position:absolute;width:108px;height:192px;border-radius:6px;overflow:hidden;background:#fff;box-shadow:0 1px 4px rgba(0,0,0,.2)}
.pcard .photo{left:0;top:0;width:108px;height:90px}
.pcard .off{position:absolute;left:4px;top:60px;height:12px;line-height:12px;background:var(--red);color:#fff;font-size:6px;padding:0 6px 0 14px;border-radius:2px}
.pcard .add{position:absolute;left:0;bottom:0;width:108px;height:22px;background:#000;color:#fff;font-size:6.5px;font-weight:700;text-align:center;line-height:22px}
.dots{position:absolute;display:flex;gap:3px}
.dots i{width:7px;height:7px;border-radius:50%}
.dash{position:absolute;border:1.3px dashed rgba(255,255,255,.9);border-radius:6px}
.pin{position:absolute;background:#fff;border-radius:8px 0 8px 8px;font-size:8.5px;color:#222;height:18px;line-height:18px;text-align:center}
.pick{position:absolute;width:105px;height:110px;border-radius:12px;background:var(--soft);text-align:center;font-size:8.5px;color:#444}
.pick svg{display:block;margin:30px auto 8px;width:26px;height:26px}
.back{position:absolute;width:12px;height:12px}
</style>
</head>
<body>
<svg width="0" height="0" style="position:absolute" aria-hidden="true">
  <defs>
    <symbol id="ic-user" viewBox="0 0 20 20"><circle cx="10" cy="10" r="8.5" fill="none" stroke="#fff" stroke-width="2"/><circle cx="10" cy="8" r="3" fill="#fff"/><path d="M4.5 15.5c1.5-2.5 3.5-3.5 5.5-3.5s4 1 5.5 3.5" fill="#fff"/></symbol>
    <symbol id="ic-search" viewBox="0 0 16 16"><circle cx="6.5" cy="6.5" r="4.7" fill="none" stroke="currentColor" stroke-width="2"/><path d="M10 10l4.5 4.5" stroke="currentColor" stroke-width="2.2" stroke-linecap="round"/></symbol>
    <symbol id="ic-spark" viewBox="0 0 16 16"><path d="M7 2l1.3 3.7L12 7l-3.7 1.3L7 12 5.7 8.3 2 7l3.7-1.3z" fill="currentColor"/><path d="M12.5 1l.6 1.4 1.4.6-1.4.6-.6 1.4-.6-1.4L10.5 3l1.4-.6z" fill="currentColor"/></symbol>
    <symbol id="ic-cart" viewBox="0 0 16 16"><path d="M1 2h2.2l2 8h7.5l1.8-6H4.4" fill="none" stroke="currentColor" stroke-width="1.8" stroke-linejoin="round"/><circle cx="6" cy="13.2" r="1.4" fill="currentColor"/><circle cx="12" cy="13.2" r="1.4" fill="currentColor"/><path d="M5 5h9l-1.3 4.3H6z" fill="currentColor"/></symbol>
    <symbol id="ic-back" viewBox="0 0 12 12"><path d="M8 1.5L3.5 6 8 10.5" fill="none" stroke="currentColor" stroke-width="2" stroke-linecap="round" stroke-linejoin="round"/></symbol>
    <symbol id="ic-go" viewBox="0 0 36 36"><circle cx="18" cy="18" r="17" fill="#000"/><path d="M11 18h13M19 12.5l5.5 5.5-5.5 5.5" fill="none" stroke="#fff" stroke-width="2.6" stroke-linecap="round" stroke-linejoin="round"/></symbol>
    <symbol id="ic-reply" viewBox="0 0 16 16"><path d="M6 3L1.5 7.5 6 12V9c4 0 6.5 1 8.5 4-.8-4.5-3.5-7-8.5-7.5z" fill="#fff"/></symbol>
    <symbol id="ic-kebab" viewBox="0 0 4 18"><circle cx="2" cy="2" r="1.8" fill="#111"/><circle cx="2" cy="9" r="1.8" fill="#111"/><circle cx="2" cy="16" r="1.8" fill="#111"/></symbol>
  </defs>
</svg>

<div class="board">

  <!-- Register -->
  <section class="screen" style="left:14px;top:14px;height:596px">
    <div class="brand">BrightLoop</div>
    <div class="title">REGISTER</div>
    <div class="field" style="left:42px;top:104px;width:192px">First Name</div>
    <div class="field" style="left:42px;top:149px;width:192px">Last Name</div>
    <div class="field" style="left:42px;top:194px;width:192px">Email</div>
    <div class="field" style="left:42px;top:238px;width:192px">Password</div>
    <div class="field" style="left:42px;top:283px;width:192px">Confirm Password</div>
    <div class="btn" style="left:76px;top:348px;width:122px">REGISTER</div>
    <div class="links" style="top:393px">Already Registered? Login</div>
    <div class="social" style="left:52px;top:442px"><div class="dot"></div><span>Register With<br>Northgate</span></div>
    <div class="social" style="left:52px;top:498px"><div class="dot"></div><span>Register With<br>Pomelo</span></div>
  </section>

  <!-- Sign in -->
  <section class="screen" style="left:303px;top:14px;height:596px">
    <div class="brand">BrightLoop</div>
    <div class="title">SIGN-IN</div>
    <div class="field" style="left:42px;top:126px;width:192px">Email</div>
    <div class="field" style="left:42px;top:179px;width:192px">Password</div>
    <div class="check" style="left:42px;top:224px"></div>
    <div class="small" style="left:67px;top:227px">Remember me</div>
    <div class="links" style="top:285px">Forgot Password<i></i>Register</div>
    <div class="btn" style="left:77px;top:321px;width:122px">SIGN-IN</div>
    <div class="btn" style="left:77px;top:366px;width:122px">SIGN-IN AS GUEST</div>
    <div class="social" style="left:52px;top:439px"><div class="dot"></div><span>Sign in with<br>Northgate</span></div>
    <div class="social" style="left:52px;top:495px"><div class="dot"></div><span>Sign in with<br>Pomelo</span></div>
  </section>

  <!-- Change password: request -->
  <section class="screen" style="left:593px;top:14px;height:596px">
    <div class="brand">BrightLoop</div>
    <div class="title">CHANGE PASSWORD</div>
    <p class="intro" style="margin:0">Lorem ipsum odor amet, consectetuer adipiscing elit. Suspendisse eleifend rhoncus nulla dictum proin interdum.</p>
    <div class="field" style="left:42px;top:163px;width:192px">Email</div>
    <div class="links" style="top:227px">Login<i></i>Register</div>
    <div class="btn" style="left:75px;top:260px;width:126px">RESET PASSWORD</div>
  </section>

  <!-- Change password: sent -->
  <section class="screen" style="left:882px;top:14px;height:596px">
    <div class="brand">BrightLoop</div>
    <div class="title">CHANGE PASSWORD</div>
    <p class="intro" style="margin:0">Lorem ipsum odor amet, consectetuer adipiscing elit. Suspendisse eleifend rhoncus nulla dictum proin interdum.</p>
    <div class="btn" style="left:75px;top:163px;width:126px">BACK TO LOGIN</div>
    <svg class="a" style="left:80px;top:206px;width:10px;height:10px" viewBox="0 0 10 10"><circle cx="5" cy="5" r="3.8" fill="none" stroke="#ccc" stroke-width="1.5"/><path d="M5 1.2A3.8 3.8 0 0 1 8.8 5" fill="none" stroke="#222" stroke-width="1.5"/></svg>
    <div class="small" style="left:98px;top:206px">Back to login page in 5s</div>
  </section>

  <!-- Change password: new -->
  <section class="screen" style="left:1171px;top:14px;height:596px">
    <div class="brand">BrightLoop</div>
    <div class="title">CHANGE PASSWORD</div>
    <p class="intro" style="margin:0">Lorem ipsum odor amet, consectetuer adipiscing elit. Suspendisse eleifend rhoncus nulla dictum proin interdum.</p>
    <div class="field" style="left:42px;top:163px;width:192px">New Password</div>
    <div class="field" style="left:42px;top:210px;width:192px">Confirm Password</div>
    <div class="links" style="top:275px">Login<i></i>Register</div>
    <div class="btn" style="left:75px;top:308px;width:126px">RESET PASSWORD</div>
  </section>

  <!-- Profile -->
  <section class="screen" style="left:14px;top:625px;height:700px">
    <div class="topbar"><div class="brand">BrightLoop</div></div>
    <svg class="back" style="left:18px;top:71px;color:#000"><use href="#ic-back"/></svg>
    <div class="btn" style="left:181px;top:65px;width:82px;height:25px;line-height:25px">&#9998; EDIT</div>
    <div class="label" style="left:21px;top:119px">FIRST NAME</div>
    <div class="field" style="left:30px;top:135px;width:216px">Firs Name</div>
    <div class="label" style="left:21px;top:182px">LAST NAME</div>
    <div class="field" style="left:30px;top:198px;width:216px">Last Name</div>
    <div class="label" style="left:21px;top:245px">DATE OF BIRTH</div>
    <div class="field" style="left:30px;top:261px;width:216px">MM - DD - YYYY</div>
    <div class="label" style="left:21px;top:308px">GENDER</div>
    <div class="a" style="left:62px;top:327px;width:29px;height:33px;background:#d6d6d6"></div>
    <div class="a" style="left:137px;top:328px;width:1px;height:31px;background:#ddd"></div>
    <div class="a" style="left:185px;top:327px;width:29px;height:33px;background:#d6d6d6"></div>
    <div class="label" style="left:21px;top:370px">EMAIL</div>
    <div class="field" style="left:30px;top:386px;width:216px">Email</div>
    <div class="label" style="left:21px;top:433px">ADDRESS</div>
    <div class="field" style="left:30px;top:449px;width:216px">Address 1, State, Country, ZIP</div>
    <div class="label" style="left:21px;top:496px">PASSWORD</div>
    <div class="field" style="left:30px;top:512px;width:216px">********</div>
    <div class="label" style="left:25px;top:559px">ADDRESS</div>
    <div class="field" style="left:34px;top:575px;width:216px">Address 1, State, Country, ZIP</div>
    <div class="btn" style="left:75px;top:639px;width:125px">&#8677; LOGOUT</div>
  </section>

  <!-- Edit profile -->
  <section class="screen" style="left:303px;top:625px;height:825px">
    <div class="topbar"><div class="brand">BrightLoop</div></div>
    <svg class="back" style="left:18px;top:66px;color:#000"><use href="#ic-back"/></svg>
    <div class="a" style="left:50px;top:63px;font-size:14px;font-weight:700;color:#111">Edit Profile</div>
    <div class="label" style="left:21px;top:110px">FIRST NAME</div>
    <div class="field" style="left:30px;top:126px;width:216px">Firs Name</div>
    <div class="label" style="left:21px;top:173px">LAST NAME</div>
    <div class="field" style="left:30px;top:189px;width:216px">Last Name</div>
    <div class="label" style="left:21px;top:236px">DATE OF BIRTH</div>
    <div class="field" style="left:30px;top:252px;width:216px">MM-DD-YYYY*</div>
    <div class="a" style="left:218px;top:263px;width:10px;height:10px;background:#ccc"></div>
    <div class="label" style="left:21px;top:299px">EMAIL</div>
    <div class="field" style="left:30px;top:315px;width:216px">Email</div>
    <div class="label" style="left:21px;top:388px">PASSWORD</div>
    <div class="field" style="left:30px;top:404px;width:216px">********</div>
    <div class="field" style="left:30px;top:446px;width:216px">********</div>
    <div class="btn-line" style="left:30px;top:488px;width:216px">CONFIRM PASSWORD</div>
    <div class="label" style="left:21px;top:561px">DELIVERY ADDRESS 1</div>
    <div class="field" style="left:30px;top:577px;width:216px">Address , State, Country, ZIP*</div>
    <div class="check" style="left:42px;top:616px"></div>
    <div class="small" style="left:67px;top:619px">Set as default delivery address</div>
    <div class="label" style="left:21px;top:646px">DELIVERY ADDRESS 2</div>
    <div class="field" style="left:30px;top:662px;width:216px">Address , State, Country, ZIP*</div>
    <div class="btn-line" style="left:31px;top:704px;width:216px">ADD ADDRESS</div>
    <div class="btn" style="left:93px;top:778px;width:91px">SAVE</div>
  </section>

  <!-- Find: upload or describe -->
  <section class="screen" style="left:593px;top:625px;height:596px">
    <div class="topbar"><div class="brand">BrightLoop</div><svg><use href="#ic-user"/></svg></div>
    <p class="intro" style="margin:0;top:78px;left:30px;width:215px">Provide an image or describe your desired fashion item below, and we'll create a personalized set of recommendations with filters to suit your needs.</p>
    <div class="pick" style="left:25px;top:129px">
      <svg viewBox="0 0 26 26"><rect x="5" y="3" width="18" height="18" rx="1.5" fill="none" stroke="#111" stroke-width="2"/><path d="M3 7v16h16" fill="none" stroke="#111" stroke-width="2"/><path d="M8 18l4-5 3 3 2-2 3 4z" fill="#111"/></svg>Upload an Image</div>
    <div class="pick" style="left:145px;top:129px">
      <svg viewBox="0 0 26 26"><path d="M3 8h5l2-3h6l2 3h5v14H3z" fill="#111"/><circle cx="13" cy="14.5" r="4.2" fill="#fff"/><path d="M13 12.5v4M11 14.5h4" stroke="#111" stroke-width="1.6"/></svg>Take a Photo</div>
    <div class="chip" style="left:17px;top:415px;width:215px">I want a white sleeveless crop top in size small</div>
    <div class="chip" style="left:17px;top:447px;width:217px;height:36px;line-height:10px;padding-top:8px;white-space:normal">I am looking for a pink floral 1950's style dress for under $200.</div>
    <div class="a" style="left:18px;top:493px;width:239px;height:33px;border-radius:17px;background:#f3f3f3;font-size:10px;color:#999;line-height:33px;padding-left:30px">
      <svg class="a" style="left:13px;top:12px;width:9px;height:9px;color:#999"><use href="#ic-search"/></svg>Describe your fashion item</div>
    <div class="nav" style="top:550px">
      <div class="on" style="left:53px"><svg><use href="#ic-search"/></svg>Search</div>
      <div style="left:138px"><svg><use href="#ic-spark"/></svg>Recommendations</div>
      <div style="left:228px"><svg><use href="#ic-cart"/></svg>Cart</div>
    </div>
  </section>

  <!-- Scanning -->
  <section class="screen" style="left:882px;top:625px;height:596px">
    <svg class="a" style="left:81px;top:69px;width:11px;height:11px" viewBox="0 0 10 10"><circle cx="5" cy="5" r="3.8" fill="none" stroke="#ccc" stroke-width="1.5"/><path d="M5 1.2A3.8 3.8 0 0 1 8.8 5" fill="none" stroke="#222" stroke-width="1.5"/></svg>
    <div class="a" style="left:98px;top:67px;font-size:11px;color:#222">Scanning Image</div>
    <div class="a center" style="top:97px;left:45px;right:45px;font-size:8px;line-height:9.5px;color:#999">One moment while we analyse the image to identify the clothing item</div>
    <div class="photo" role="img" aria-label="Photo of a model in a black crop top, white track pants and sneakers, crouching by a wall" style="left:27px;top:165px;width:221px;height:376px;border-radius:10px"></div>
    <div class="a" style="left:0;top:588px;width:275px;height:8px;background:#c4c4c4"></div>
    <div class="a" style="left:0;top:588px;width:93px;height:8px;background:#000"></div>
  </section>

  <!-- Completed scan -->
  <section class="screen" style="left:1171px;top:625px;height:596px">
    <div class="a center" style="top:67px;font-size:11px;color:#222">Completed Scan</div>
    <div class="a center" style="top:97px;left:55px;right:55px;font-size:8px;line-height:9.5px;color:#999">Select the item of clothing you wish to search for</div>
    <div class="photo" role="img" aria-label="Scanned photo of a model in a black crop top, white track pants and sneakers" style="left:27px;top:165px;width:221px;height:376px;border-radius:10px"></div>
    <div class="dash" style="left:81px;top:272px;width:93px;height:58px"></div>
    <div class="pin" style="left:139px;top:275px;width:36px">Top</div>
    <div class="dash" style="left:81px;top:333px;width:155px;height:77px"></div>
    <div class="pin" style="left:191px;top:336px;width:45px">Bottom</div>
    <div class="dash" style="left:81px;top:427px;width:94px;height:64px"></div>
    <div class="pin" style="left:132px;top:430px;width:43px">Shoes</div>
  </section>

  <!-- Recommendations list -->
  <section class="screen" style="left:14px;top:1340px;height:597px">
    <div class="topbar"><div class="brand">BrightLoop</div><svg><use href="#ic-user"/></svg></div>
    <div class="a" role="img" aria-label="Promotional banner photo of a smiling model in sunglasses" style="left:0;top:44px;width:275px;height:121px;background:linear-gradient(90deg,#f0a21a,#f7b42a 55%,#fbc13d)"></div>
    <div class="a" style="left:131px;top:76px;font-size:22px;font-weight:700;line-height:26px;color:#fff">PROMOTE<br>HERE</div>
    <div class="dots" style="left:120px;top:146px"><i style="background:#fff;width:12px;border-radius:4px"></i><i style="background:#fff;opacity:.6"></i><i style="background:#fff;opacity:.6"></i></div>
    <div class="a" style="left:14px;top:180px;font-size:13px;font-weight:500;color:#444">20 Items</div>
    <div class="a" style="left:189px;top:179px;width:72px;height:20px;border:1px solid #333;border-radius:10px;font-size:10px;text-align:center;line-height:18px;color:#222">&#8595; Price</div>
    <div class="check" style="left:14px;top:207px"></div>
    <div class="small" style="left:39px;top:210px">Show free shipping only</div>
    <div class="a" style="left:14px;top:245px;font-size:13.5px;font-weight:500;color:#444">Direct Match</div>
    <div class="pcard" style="left:20px;top:273px">
      <div class="photo" role="img" aria-label="Product photo of a model in a crop top and track pants"></div>
      <div class="off">30% OFF</div>
      <div class="a" style="left:13px;top:98px;font-size:8px;color:#333">Product Name</div>
      <div class="a" style="left:13px;top:111px;font-size:5.5px;color:#999">Nearest Location</div>
      <div class="dots" style="left:13px;top:124px"><i style="border:1px solid #ccc"></i><i style="background:#333"></i><i style="background:#5aa6ee"></i><i style="background:#c9a27a"></i></div>
      <div class="a" style="right:8px;top:146px;font-size:10px;font-weight:700;color:#111"><s style="font-size:5.5px;color:#999;font-weight:400">$66.00</s> $66.00</div>
      <div class="add">&#9707; ADD TO CART</div>
    </div>
    <div class="pcard" style="left:147px;top:273px">
      <div class="photo" role="img" aria-label="Product photo of a model in a crop top and track pants"></div>
      <div class="a" style="left:13px;top:98px;font-size:8px;color:#333">Product Name</div>
      <div class="a" style="left:13px;top:111px;font-size:5.5px;color:#999">Nearest Location</div>
      <div class="dots" style="left:13px;top:124px"><i style="border:1px solid #ccc"></i><i style="background:#333"></i><i style="background:#5aa6ee"></i><i style="background:#c9a27a"></i></div>
      <div class="a" style="right:8px;top:146px;font-size:10px;font-weight:700;color:#111"><s style="font-size:5.5px;color:#999;font-weight:400">$66.00</s> $66.00</div>
      <div class="add">&#9707; ADD TO CART</div>
    </div>
    <div class="a" style="left:14px;top:492px;font-size:13.5px;font-weight:500;color:#444">Similar Match</div>
    <div class="photo" role="img" aria-label="Similar product photo" style="left:20px;top:520px;width:108px;height:40px;border-radius:6px 6px 0 0"></div>
    <div class="photo" role="img" aria-label="Similar product photo" style="left:147px;top:520px;width:108px;height:40px;border-radius:6px 6px 0 0"></div>
    <div class="nav" style="top:550px">
      <div style="left:53px"><svg><use href="#ic-search"/></svg>Search</div>
      <div class="on" style="left:138px"><svg><use href="#ic-spark"/></svg>Recommendations</div>
      <div style="left:228px"><svg><use href="#ic-cart"/></svg>Cart</div>
    </div>
  </section>

  <!-- Store chat -->
  <section class="screen" style="left:303px;top:1465px;height:595px">
    <div class="photo" role="img" aria-label="Product photo of a model in a crop top and track pants" style="left:0;top:0;width:275px;height:190px"></div>
    <svg class="back" style="left:18px;top:28px;color:#fff"><use href="#ic-back"/></svg>
    <div class="a" style="left:0;top:180px;width:275px;height:415px;background:#fff;border-radius:18px 18px 0 0"></div>
    <div class="a" style="left:65px;top:190px;width:149px;height:3px;border-radius:2px;background:#888"></div>
    <div class="a" style="left:21px;top:218px;width:217px;height:54px;border-radius:12px;background:#000;color:#fff;font-size:8.5px;line-height:54px;padding-left:18px">Does this store offer free returns?</div>
    <div class="a" style="left:213px;top:226px;width:38px;height:38px;border-radius:50%;background:#fff;border:3px solid #000"><svg style="width:100%;height:100%" viewBox="0 0 20 20"><circle cx="10" cy="10" r="8.5" fill="none" stroke="#000" stroke-width="2"/><circle cx="10" cy="8" r="3" fill="#000"/><path d="M4.5 15.5c1.5-2.5 3.5-3.5 5.5-3.5s4 1 5.5 3.5" fill="#000"/></svg></div>
    <div class="a" style="right:38px;top:279px;font-size:8px;color:#aaa">20th Sept</div>
    <div class="a" style="left:22px;top:363px;width:32px;height:32px;border-radius:50%;background:#000"><svg class="a" style="left:9px;top:9px;width:14px;height:14px;color:#fff"><use href="#ic-search"/></svg></div>
    <div class="a" style="left:39px;top:316px;width:215px;height:128px;border:1.3px solid #555;border-radius:10px;font-size:8.3px;line-height:16.8px;color:#888;padding:12px 14px 0 28px">A flat, $10 free for a prepaid shipping label is payable by the customer during the Returns Portal process. A returns tracking link will be emailed to you when you finalise your return.</div>
    <div class="a" style="left:39px;top:451px;font-size:8px;color:#aaa">20th Sept</div>
    <div class="chip" style="left:17px;top:503px;width:123px">What size is the model?</div>
    <div class="chip" style="left:152px;top:503px;width:140px">How much is express shipping?</div>
    <div class="a" style="left:17px;top:540px;width:241px;height:33px;border:1.5px solid #ddd;border-radius:17px;font-size:10px;color:#999;line-height:30px;padding-left:14px">Message<span style="position:absolute;right:12px;color:#777">&#10148;</span></div>
  </section>

  <!-- Product detail -->
  <section class="screen" style="left:593px;top:1236px;height:696px">
    <div class="topbar"><div class="brand">BrightLoop</div><svg><use href="#ic-user"/></svg></div>
    <div class="photo" role="img" aria-label="Product photo of a model in a black crop top and white track pants" style="left:0;top:44px;width:275px;height:193px"></div>
    <svg class="back" style="left:18px;top:72px;color:#111"><use href="#ic-back"/></svg>
    <div class="badge" style="top:182px">30% OFF</div>
    <div class="a" style="left:14px;top:259px;font-size:13px;font-weight:500;color:#222">Product Name</div>
    <div class="a" style="right:14px;top:255px;font-size:19px;font-weight:700;color:#111"><s style="font-size:10px;color:#999;font-weight:400;margin-right:4px">$66.00</s>$66.00</div>
    <div class="sizes" style="left:14px;top:290px"><span>S</span><span>M</span><span>L</span><span>XL</span></div>
    <div class="swatch" style="left:14px;top:321px;background:var(--c-coral)"></div>
    <div class="swatch" style="left:38px;top:321px;background:var(--c-teal)"></div>
    <div class="swatch" style="left:62px;top:321px;background:var(--c-slate)"></div>
    <div class="tag" style="left:166px;top:321px;width:94px">Free Shipping</div>
    <div class="tabs" style="left:23px;top:368px"><span class="on">Description</span><span>Features</span><span>Shipping</span><span>Store Info</span></div>
    <p class="desc" style="left:20px;top:388px;margin:0">Lorem ipsum odor amet, consectetuer adipiscing elit. Habitasse neque rhoncus lobortis vehicula hendrerit vel dapibus. Urna cursus facilisis senectus pulvinar neque laoreet venenatis. Ex feugiat felis fermentum laoreet class semper? Orci aliquam nulla mus sapien lorem porttitor venenatis nisi quisque. Eleifend elementum sem efficitur lobortis arcu. Turpis ridiculus vestibulum; faucibus adipiscing morbi at platea dictum.</p>
    <div class="chip" style="left:17px;top:553px;width:122px">What size is the model?</div>
    <div class="chip" style="left:151px;top:553px;width:140px">How much is express shipping?</div>
    <div class="ask" style="left:17px;top:587px;width:242px"><svg><use href="#ic-go"/></svg></div>
    <div class="buybar" style="top:646px"><div>ADD TO CART</div><div>BUY NOW</div></div>
  </section>

  <!-- Product detail: out of stock -->
  <section class="screen" style="left:882px;top:1236px;height:696px">
    <div class="topbar"><div class="brand">BrightLoop</div><svg><use href="#ic-user"/></svg></div>
    <div class="photo" role="img" aria-label="Dimmed product photo of a model in a black crop top and white track pants" style="left:0;top:44px;width:275px;height:193px;background:linear-gradient(160deg,#8a8a8a,#6d6d6d 45%,#4f4f4f)"></div>
    <svg class="back" style="left:18px;top:72px;color:#fff"><use href="#ic-back"/></svg>
    <div class="a center" style="top:132px;font-size:14px;font-weight:700;color:#fff">Out Of Stock</div>
    <div class="badge" style="top:182px">30% OFF</div>
    <div class="a" style="left:14px;top:259px;font-size:13px;font-weight:500;color:#222">Product Name</div>
    <div class="a" style="right:14px;top:255px;font-size:19px;font-weight:700;color:#111"><s style="font-size:10px;color:#999;font-weight:400;margin-right:4px">$66.00</s>$66.00</div>
    <div class="sizes" style="left:14px;top:290px"><span>S</span><span>M</span><span>L</span><span>XL</span></div>
    <div class="swatch" style="left:14px;top:321px;background:var(--c-coral)"></div>
    <div class="swatch" style="left:38px;top:321px;background:var(--c-teal)"></div>
    <div class="swatch" style="left:62px;top:321px;background:var(--c-slate)"></div>
    <div class="tag" style="left:166px;top:321px;width:94px">Free Shipping</div>
    <div class="tabs" style="left:23px;top:368px"><span class="on">Description</span><span>Features</span><span>Shipping</span><span>Store Info</span></div>
    <p class="desc" style="left:20px;top:388px;margin:0">Lorem ipsum odor amet, consectetuer adipiscing elit. Habitasse neque rhoncus lobortis vehicula hendrerit vel dapibus. Urna cursus facilisis senectus pulvinar neque laoreet venenatis. Ex feugiat felis fermentum laoreet class semper? Orci aliquam nulla mus sapien lorem porttitor venenatis nisi quisque. Eleifend elementum sem efficitur lobortis arcu. Turpis ridiculus vestibulum; faucibus adipiscing morbi at platea dictum.</p>
    <div class="chip" style="left:17px;top:553px;width:122px">What size is the model?</div>
    <div class="chip" style="left:151px;top:553px;width:140px">How much is express shipping?</div>
    <div class="ask" style="left:17px;top:587px;width:242px"><svg><use href="#ic-go"/></svg></div>
    <div class="buybar" style="top:646px"><div>ADD TO CART</div><div>BUY NOW</div></div>
  </section>

  <!-- Cart -->
  <section class="screen" style="left:1171px;top:1236px;height:596px">
    <div class="topbar"><div class="brand">BrightLoop</div><svg><use href="#ic-user"/></svg></div>
    <div class="btn" style="left:38px;top:62px;width:200px"><svg style="width:13px;height:13px;vertical-align:-2px;margin-right:6px"><use href="#ic-reply"/></svg>CONTINUE SHOPPING</div>
    <div class="card" style="left:18px;top:112px;width:239px;height:189px">
      <div class="store"><div class="radio"></div><div class="avatar"></div><b>Store Name</b><svg class="kebab"><use href="#ic-kebab"/></svg></div>
      <div class="item" style="top:58px">
        <div class="thumb" role="img" aria-label="Product thumbnail"></div>
        <div class="iname" style="top:0">Product Name</div>
        <div class="imeta" style="top:14px">Size, Color</div>
        <div class="price" style="right:8px;top:0">$66.00</div>
        <div class="step" style="left:165px;top:22px"><div class="pm">&minus;</div><div class="qty">1</div><div class="pm">+</div></div>
      </div>
      <div class="item" style="top:131px">
        <div class="thumb" role="img" aria-label="Product thumbnail"></div>
        <div class="iname" style="top:0">Product Name</div>
        <div class="imeta" style="top:14px">Size, Color</div>
        <div class="price" style="right:8px;top:0">$66.00</div>
        <div class="step" style="left:165px;top:22px"><div class="pm">&minus;</div><div class="qty">1</div><div class="pm">+</div></div>
      </div>
    </div>
    <div class="card" style="left:18px;top:323px;width:239px;height:117px">
      <div class="store"><div class="radio"></div><div class="avatar"></div><b>Store Name</b><svg class="kebab"><use href="#ic-kebab"/></svg></div>
      <div class="item" style="top:57px">
        <div class="thumb" role="img" aria-label="Product thumbnail"></div>
        <div class="iname" style="top:0">Product Name</div>
        <div class="price" style="right:8px;top:0">$66.00</div>
        <div class="select" style="left:62px;top:12px;width:67px">Size</div>
        <div class="select" style="left:135px;top:12px;width:67px">Color</div>
      </div>
    </div>
    <div class="totalbar" style="top:457px"><span style="left:17px">Total</span><span style="right:18px;font-weight:700">$1,234.00</span></div>
    <div class="checkout" style="top:505px"><svg style="width:12px;height:12px;vertical-align:-2px;margin-right:6px;color:#fff"><use href="#ic-cart"/></svg>CHECKOUT</div>
    <div class="nav" style="top:550px">
      <div style="left:53px"><svg><use href="#ic-search"/></svg>Search</div>
      <div style="left:138px"><svg><use href="#ic-spark"/></svg>Recommendations</div>
      <div class="on" style="left:228px"><svg><use href="#ic-cart"/></svg>Cart</div>
    </div>
  </section>

  <!-- Cart: swipe to remove -->
  <section class="screen" style="left:1475px;top:1236px;height:596px">
    <div class="topbar"><div class="brand">BrightLoop</div><svg><use href="#ic-user"/></svg></div>
    <div class="btn" style="left:38px;top:62px;width:200px"><svg style="width:13px;height:13px;vertical-align:-2px;margin-right:6px"><use href="#ic-reply"/></svg>CONTINUE SHOPPING</div>
    <div class="card" style="left:17px;top:112px;width:240px;height:244px">
      <div class="store"><div class="radio"></div><div class="avatar"></div><b>Store Name</b><svg class="kebab"><use href="#ic-kebab"/></svg></div>
      <div class="item" style="top:58px">
        <div class="thumb" role="img" aria-label="Product thumbnail"></div>
        <div class="iname" style="top:0">Product Name</div>
        <div class="imeta" style="top:14px">Size, Color</div>
        <div class="price" style="left:137px;top:0">$66.00</div>
        <div class="step" style="left:66px;top:35px"><div class="pm">&minus;</div><div class="qty">1</div><div class="pm">+</div></div>
      </div>
      <div class="a" style="left:0;width:187px;top:139px;height:1px;background:#e4e4e4"></div>
      <div class="item" style="top:165px">
        <div class="thumb" role="img" aria-label="Product thumbnail"></div>
        <div class="iname" style="top:0">Product Name</div>
        <div class="imeta" style="top:14px">Size, Color</div>
        <div class="price" style="left:137px;top:0">$66.00</div>
        <div class="step" style="left:66px;top:38px"><div class="pm">&minus;</div><div class="qty">1</div><div class="pm">+</div></div>
      </div>
      <div class="swipe" style="left:187px;top:41px;width:53px;height:98px"></div>
      <div class="swipe" style="left:187px;top:140px;width:53px;height:104px"></div>
    </div>
    <div class="card" style="left:17px;top:379px;width:240px;height:100px">
      <div class="store"><div class="radio"></div><div class="avatar"></div><b>Store Name</b><svg class="kebab"><use href="#ic-kebab"/></svg></div>
      <div class="item" style="top:57px">
        <div class="thumb" role="img" aria-label="Product thumbnail"></div>
        <div class="iname" style="top:0">Product Name</div>
        <div class="price" style="right:8px;top:0">$66.00</div>
      </div>
    </div>
    <div class="totalbar" style="top:457px"><span style="left:17px">Total</span><span style="right:18px;font-weight:700">$1,234.00</span></div>
    <div class="checkout" style="top:505px"><svg style="width:12px;height:12px;vertical-align:-2px;margin-right:6px;color:#fff"><use href="#ic-cart"/></svg>CHECKOUT</div>
    <div class="nav" style="top:550px">
      <div style="left:53px"><svg><use href="#ic-search"/></svg>Search</div>
      <div style="left:138px"><svg><use href="#ic-spark"/></svg>Recommendations</div>
      <div class="on" style="left:228px"><svg><use href="#ic-cart"/></svg>Cart</div>
    </div>
  </section>

</div>
</body>
</html>
```